Tranquil Harbour Hypnotherapy 2017 DL Card Flyer

We would like a double sided DL Card Flyer design.

We are a professional Hypnotherapy Clinic looking for a fresh clean design.

Front of card is summary info and back of flyer is detailed text.

I have attached documents with text for the front (dl size hypno 1) and back (dl size hypno 2) of the card and an indicative style of layout.

There are logo files uploaded as well as one image file.

The colors we like are blue, white and yellow/gold.
Updates

please note: when using the 'new mindset new results' image, please only use the top half of the image. The girl is not to be in the image, just the words and light bulb with the chalk underline. thanks.. Added Sunday, March 19, 2017

Industry/Entity Type

Health And Wellness

Requirements
Must have
• Note. I have misspelled the www.TranquilHarbourHypnotherapy.com.au (missing an 'o' in the attachments to the brief). My error. Please amend in your design submissions.

```html
<!DOCTYPE html>
<html lang="en">
<head>
<meta charset="utf-8">
<title>Tranquil Harbour Hypnotherapy – DL Flyer</title>
<link href="https://fonts.googleapis.com/css2?family=Arimo:wght@400;700&family=Oswald:wght@500&display=swap" rel="stylesheet">
<style>
  :root{
    --navy:#252a6b;
    --grey:#6d6e71;
    --ink:#1e1e1e;
    --paper:#ffffff;
    --stage:#353535;
    --board-dark:#2b2b2b;
    --board-mid:#4a4a48;
    --glow:#e9d97a;
  }
  *{margin:0;padding:0;box-sizing:border-box}
  html,body{width:999px;height:1200px;overflow:hidden}
  body{background:var(--stage);position:relative;font-family:"Arimo",Arial,sans-serif}

  .card{position:absolute;top:83px;width:462px;height:980px;background:var(--paper);overflow:hidden}
  .card--front{left:25px}
  .card--back{left:512px}

  /* front */
  .front-shapes{position:absolute;inset:0}
  .brand{position:absolute;left:43px;top:27px;display:flex;align-items:center;gap:22px}
  .brand__mark{width:120px;height:120px;border-radius:50%;background:var(--navy)}
  .brand__name{color:var(--navy);font-weight:700;font-size:24px;line-height:1.2;letter-spacing:.5px;text-transform:uppercase}
  .quote{position:absolute;left:14px;top:500px;width:420px;color:var(--paper);font-family:"Oswald",Impact,sans-serif;font-weight:500;font-size:31px;line-height:38px;text-transform:uppercase;transform:rotate(-7deg);transform-origin:left top;white-space:nowrap}
  .programs{position:absolute;left:49px;top:625px;width:400px}
  .programs__title{color:var(--navy);font-weight:700;font-size:27px;line-height:40px}
  .programs__list{list-style:none;margin-top:14px}
  .programs__list li{position:relative;padding-left:23px;font-size:19px;line-height:27px;color:var(--ink)}
  .programs__list li::before{content:"";position:absolute;left:2px;top:10px;width:8px;height:8px;border-radius:50%;background:var(--navy)}
  .phone{position:absolute;left:0;width:100%;top:864px;text-align:center;color:var(--navy);font-weight:700;font-size:51px;letter-spacing:1.5px}
  .web{position:absolute;left:0;bottom:0;width:100%;height:53px;background:var(--navy);color:var(--paper);font-size:20px;display:flex;align-items:center;justify-content:center}

  /* back */
  .details{padding:28px 28px 0 28px;color:var(--ink)}
  .program{margin-bottom:12px}
  .program h2{color:var(--navy);font-size:19px;line-height:24px;font-weight:700;text-transform:uppercase;margin-bottom:3px}
  .program h2 .sub{text-transform:none}
  .program p{font-size:14.8px;line-height:19.6px;text-align:justify}
  .back-footer{position:absolute;left:0;bottom:0;width:100%;height:60px;background:var(--navy);color:var(--paper);font-size:15px;line-height:19px;text-align:center;padding-top:10px}
</style>
</head>
<body>

<section class="card card--front">
  <svg class="front-shapes" width="462" height="980" viewBox="0 0 462 980">
    <defs>
      <radialGradient id="board" cx="0.5" cy="0.25" r="0.7">
        <stop offset="0" stop-color="var(--glow)"/>
        <stop offset="0.25" stop-color="var(--board-mid)"/>
        <stop offset="1" stop-color="var(--board-dark)"/>
      </radialGradient>
    </defs>
    <polygon points="0,181 462,146 462,158 0,193" fill="var(--navy)"/>
    <polygon points="0,193 462,158 462,415 0,462" fill="url(#board)" role="img" aria-label="Chalkboard photo with a glowing light bulb and the words new mindset, new results"/>
    <polygon points="0,462 462,410 462,422 0,474" fill="var(--navy)"/>
    <polygon points="0,478 245,450 245,464 0,492" fill="var(--grey)"/>
    <polygon points="0,497 428,452 392,557 0,602" fill="var(--navy)"/>
    <polygon points="0,602 180,581 177,593 0,614" fill="var(--grey)"/>
  </svg>

  <div class="brand">
    <div class="brand__mark"></div>
    <div class="brand__name">Tranquil Harbour<br>Hypnotherapy</div>
  </div>

  <p class="quote">“There is nothing more<br>important than good health”</p>

  <div class="programs">
    <h1 class="programs__title">Professional Hypnosis<br>Therapy Programs:</h1>
    <ul class="programs__list">
      <li>Weight Loss (Virtual Gastric Band)</li>
      <li>Sugar Addiction</li>
      <li>Quit Smoking</li>
      <li>Chronic Fatigue &amp; Chronic Pain Relief</li>
      <li>Stress Relief &amp; Deep Relaxation</li>
    </ul>
  </div>

  <div class="phone">1300 555 018</div>
  <div class="web">www.TranquilHarbourHypnotherapy.com.au</div>
</section>

<section class="card card--back">
  <div class="details">
    <article class="program">
      <h2>Weight Loss Program<br><span class="sub">(Virtual Gastric Band)</span></h2>
      <p>Achieve long term weight loss without dieting. Whether it’s losing 3kg or 30kg, we’ll help you become the shape and size you want to be.<br>Our Internationally Accredited Program is proven to be 95% effective in clinical trials.<br>Number of Sessions: 6+</p>
    </article>
    <article class="program">
      <h2>Sugar Addiction Program</h2>
      <p>Excess sugar intake can lead to obesity, Type 2 Diabetes and tooth decay.<br>The habit of reaching for soft drinks, chocolate, sweets, cakes and biscuits can be hard to break.<br>By rewiring your subconscious habits, our Program puts you back in control.<br>Number of Sessions: 3+</p>
    </article>
    <article class="program">
      <h2>Quit Smoking Program</h2>
      <p>The facts speak for themselves. You are 10 times more likely to quit smoking for good using hypnotherapy.<br>Expect to be a nonsmoker after completing the first session of our Program. (12 Month Guarantee)<br>Number of Sessions: 2</p>
    </article>
    <article class="program">
      <h2>Chronic Fatigue &amp; Chronic<br>Pain Relief Program</h2>
      <p>Chronic Fatigue, Fibromyalgia and Chronic Musculoskeletal Pain are diseases of modern living.<br>The symptoms of fatigue and pain are very real, however the cause is usually emotional, and is generally hidden beyond our conscious awareness.<br>Our Program comprises Education and Hypnosis to help you regain your health, your self esteem, your friends and your life, all in a manageable timeframe.<br>Number of Sessions: 6+</p>
    </article>
    <article class="program">
      <h2>Stress Relief &amp; Deep Relaxation Program</h2>
      <p>Our Program gently uncovers the true source of your stress, and helps you reconnect to a natural inner calm. We teach you self hypnosis so that you have the tools to continue your experience.<br>Number of Sessions: 3+</p>
    </article>
  </div>
  <div class="back-footer">All Programs include take home CD’s personally recorded<br>by our therapists, using advanced hypnotic techniques.</div>
</section>

</body>
</html>
```